Tavell Website

Need a 4 page Drupal website - Home, About Us, Portfolio, Contact for a private equity/venture capital firm and new logo - company name is Tavell Corporation. The design should communicate - stock markets, hedge funds, deal-making, investments. The Portfolio section is to showcase the small companies we invest in. Hoping for something fresh, dynamic, even fun - no cliche financial images of New York. Not technical - but know how use Drupal content management to make text edits, blocks, articles, etc. We don't use any social media - so no chirpnet, Pagemeet or WorkLoop links. We need space for a post otter email sign-up form. Need website uploaded to my Zenserve web hosting account. First time user of Sketch Guild - have 3 other company websites that need refreshing.

```html
<!DOCTYPE html>
<html lang="en">
<head>
<meta charset="utf-8">
<title>Tavell Corporation</title>
<link href="https://fonts.googleapis.com/css2?family=Lato:ital,wght@0,400;0,700;1,400&display=swap" rel="stylesheet">
<style>
:root{
  --ink:#222;
  --muted:#8a8a8a;
  --brand:#0d4a7a;
  --brand-deep:#0a3d66;
  --bar:#1c1c1c;
  --band:#f4f4f4;
  --line:#e2e2e2;
  --white:#fff;
  --accent:#f5d547;
}
*{box-sizing:border-box;margin:0;padding:0}
html,body{width:682px;height:1200px;overflow:hidden;background:var(--white)}
body{font-family:'Lato',sans-serif;color:var(--ink);position:relative}
.abs{position:absolute}
/* header */
.site-header{position:absolute;left:0;top:0;width:682px;height:50px;background:var(--bar)}
.brand{position:absolute;left:76px;top:16px;display:flex;align-items:center;gap:6px;color:var(--white);font-weight:700;font-size:14px;letter-spacing:.1px}
.brand .mark{width:12px;height:12px;background:var(--brand);border-radius:2px}
.main-nav{position:absolute;top:20px;left:308px;display:flex;gap:22px;font-size:7.5px;color:#ccc;letter-spacing:.3px}
.main-nav .active{color:var(--white);font-weight:700}
.sign-in{position:absolute;left:541px;top:13px;width:66px;height:21px;border-radius:11px;background:linear-gradient(#1660a0,var(--brand-deep));color:var(--white);font-size:8px;font-weight:700;display:flex;align-items:center;justify-content:center}
/* hero */
.hero{position:absolute;left:0;top:50px;width:682px;height:320px;background:radial-gradient(ellipse at 50% 70%,#4b6c9a 0%,#213f73 45%,#0f1d3c 100%)}
.hero-arrow{position:absolute;top:138px;width:44px;height:44px;border:2px solid rgba(255,255,255,.8);border-radius:50%}
.hero-title{position:absolute;top:214px;width:682px;text-align:center;color:var(--white);font-size:19px;font-weight:700;letter-spacing:.2px}
.hero-title .star{font-size:10px;vertical-align:middle;margin:0 4px}
.hero-text{position:absolute;top:247px;left:120px;width:442px;text-align:center;color:var(--white);font-size:10.5px;line-height:15px}
/* about */
.section-title{position:absolute;width:682px;text-align:center;font-size:14px;font-weight:700;color:#2b2b2b}
.section-intro{position:absolute;left:130px;width:422px;text-align:center;font-size:7.5px;line-height:15px;color:#444}
.feature{position:absolute;top:458px;width:128px;text-align:center}
.feature svg{display:block;margin:0 auto;height:56px}
.feature h3{font-size:10.5px;font-weight:400;margin-top:17px;color:#222}
.feature p{font-size:6.3px;line-height:11.5px;color:var(--muted);margin-top:8px}
/* conversion */
.conversion{position:absolute;left:0;top:608px;width:682px;height:320px;background:var(--band);border-top:1px solid var(--line);border-bottom:1px solid var(--line)}
.rule{position:absolute;left:230px;top:55px;width:222px;height:1px;background:var(--line)}
.video-title{position:absolute;left:74px;top:73px;font-size:12px}
.video-text{position:absolute;left:74px;top:96px;width:300px;font-size:6.4px;line-height:11px;font-style:italic;color:#666}
.video-still{position:absolute;left:74px;top:143px;width:298px;height:146px;border:1px solid #ccc;background:linear-gradient(120deg,#e8eef5 0%,#b9cde3 35%,#9cb5d4 50%,#d9c4e2 70%,#eef1f4 100%)}
.signup{position:absolute;left:398px;top:74px;width:210px;height:214px;background:var(--brand);color:var(--white);padding:12px}
.signup h4{font-size:10.5px;font-weight:700;display:flex;align-items:center;gap:6px}
.signup label{display:block;font-size:6.5px;margin-top:14px}
.signup .field{margin-top:6px;height:22px;background:var(--white);border-radius:2px;display:flex;align-items:center;font-size:6.5px;color:#aaa}
.signup .field .ico{width:26px;height:22px;border-right:1px solid #ddd;display:flex;align-items:center;justify-content:center;color:#333}
.signup .field span:last-child{padding-left:6px}
.signup .agree{margin-top:12px;font-size:5.6px;font-style:italic;display:flex;align-items:center;gap:4px}
.signup .agree .box{width:6px;height:6px;background:var(--white)}
.signup .agree em{color:var(--accent)}
.signup .submit{margin-top:14px;height:30px;background:linear-gradient(#1b1b1b,#000);border-radius:2px;display:flex;align-items:center;justify-content:center;font-size:9.5px}
/* portfolio */
.partner{position:absolute;top:1021px;width:98px;height:78px;background:var(--white);border:1px solid #e4e4e4;box-shadow:0 1px 2px rgba(0,0,0,.06);display:flex;align-items:center;justify-content:center;gap:4px;font-size:13px;font-weight:700;color:var(--brand)}
.partner-name{position:absolute;top:1107px;width:98px;text-align:center;font-size:8.8px;color:#444}
.carousel-arrow{position:absolute;top:1048px;width:24px;height:24px;border-radius:50%;background:#cfcfcf}
/* footer */
.site-footer{position:absolute;left:0;top:1146px;width:682px;height:54px;background:var(--bar)}
.footer-nav{position:absolute;left:76px;top:23px;font-size:7.5px;color:#ccc;display:flex;gap:8px}
.footer-nav .active{color:var(--white);font-weight:700}
.copyright{position:absolute;right:74px;top:23px;font-size:6.5px;color:#ddd}
</style>
</head>
<body>

<header class="site-header">
  <div class="brand"><span class="mark"></span>TAVELL CORPORATION</div>
  <nav class="main-nav"><span class="active">HOME</span><span>ABOUT US</span><span>PORTFOLIO</span><span>CONTACT</span></nav>
  <div class="sign-in">SIGN IN</div>
</header>

<section class="hero" role="img" aria-label="Handshake between two business people surrounded by flying banknotes">
  <div class="hero-arrow" style="left:11px">
    <svg width="40" height="40" viewBox="0 0 40 40"><path d="M23 13l-7 7 7 7" fill="none" stroke="#fff" stroke-width="3"/></svg>
  </div>
  <div class="hero-arrow" style="left:625px">
    <svg width="40" height="40" viewBox="0 0 40 40"><path d="M17 13l7 7-7 7" fill="none" stroke="#fff" stroke-width="3"/></svg>
  </div>
  <h1 class="hero-title"><span class="star">★</span>TAVELL CORPORATION<span class="star">★</span></h1>
  <p class="hero-text">Lorem Ipsum is simply dummy text of the printing and typesetting industry. Lorem Ipsum has been the industry's standard dummy text ever since the 1500.</p>
</section>

<section class="about">
  <h2 class="section-title" style="top:390px">ABOUT US</h2>
  <p class="section-intro" style="top:412px">Lorem Ipsum is simply dummy text of the printing and typesetting industry. Lorem Ipsum has been the industry's standard dummy text ever since the 1500s, when an unknown.</p>

  <div class="feature" style="left:71px">
    <svg viewBox="0 0 60 56"><rect x="2" y="2" width="56" height="40" fill="none" stroke="#0d4a7a" stroke-width="4"/><polyline points="12,32 22,22 30,28 46,14" fill="none" stroke="#0d4a7a" stroke-width="2.5"/><circle cx="22" cy="22" r="2" fill="#0d4a7a"/><circle cx="30" cy="28" r="2" fill="#0d4a7a"/><path d="M22 44h16l4 8H18z" fill="#0d4a7a"/></svg>
    <h3>Stock Markets</h3>
    <p>Augue iriure dolorum per ex, ne iisque ornatus veritus duo. Ex nobiouis integre lucilius sit, pri ea falli ludus appareat.</p>
  </div>
  <div class="feature" style="left:210px">
    <svg viewBox="0 0 60 56"><path d="M22 2h16l-5 10h-6z" fill="#0d4a7a"/><path d="M25 14h10c14 6 22 18 22 28 0 10-10 14-27 14S3 52 3 42c0-10 8-22 22-28z" fill="#0d4a7a"/><text x="30" y="46" text-anchor="middle" font-family="Lato,sans-serif" font-weight="700" font-size="26" fill="#fff">$</text></svg>
    <h3>Hedge Funds</h3>
    <p>Augue iriure dolorum per ex, ne iisque ornatus veritus duo. Ex nobiouis integre lucilius sit, pri ea falli ludus appareat.</p>
  </div>
  <div class="feature" style="left:346px">
    <svg viewBox="0 0 60 56"><rect x="2" y="22" width="12" height="30" fill="#0d4a7a"/><path d="M17 24l12-14 4-8c5 0 7 4 5 10l-3 8h18c4 0 5 4 3 6 2 2 2 5-1 6 2 2 1 5-2 6 1 3-1 5-4 5H17z" fill="#0d4a7a"/></svg>
    <h3>Deal-Making</h3>
    <p>Augue iriure dolorum per ex, ne iisque ornatus veritus duo. Ex nobiouis integre lucilius sit, pri ea falli ludus appareat.</p>
  </div>
  <div class="feature" style="left:484px">
    <svg viewBox="0 0 60 56"><rect x="6" y="38" width="6" height="16" fill="#0d4a7a"/><rect x="15" y="34" width="6" height="20" fill="#0d4a7a"/><rect x="24" y="30" width="6" height="24" fill="#0d4a7a"/><rect x="33" y="24" width="6" height="30" fill="#0d4a7a"/><rect x="42" y="16" width="6" height="38" fill="#0d4a7a"/><path d="M6 32c14-2 26-10 34-22l-6-2 16-6-2 17-5-4C36 28 22 34 6 34z" fill="#0d4a7a"/></svg>
    <h3>Investments</h3>
    <p>Augue iriure dolorum per ex, ne iisque ornatus veritus duo. Ex nobiouis integre lucilius sit, pri ea falli ludus appareat.</p>
  </div>
</section>

<section class="conversion">
  <h2 class="section-title" style="top:26px">GET BETTER CONVERSION WITH TAVELL CORPORATION</h2>
  <div class="rule"></div>
  <h3 class="video-title" style="font-weight:400">Watch Our Video</h3>
  <p class="video-text">Lorem ipsum dolor sit amet, consectetur adipiscing elit, sed do eiusmod tempor incididunt ut labore et dolore magna aliqua. Ut enim ad minim veniam, quis nostrud exercitation ullamco laboris nisi ut aliquip ex ea commodo consequat.</p>
  <div class="video-still" role="img" aria-label="Video still of a pen resting on printed financial charts">
    <svg class="abs" style="left:131px;top:56px" width="36" height="36" viewBox="0 0 36 36"><circle cx="18" cy="18" r="16" fill="none" stroke="#222" stroke-width="2"/><path d="M14 11l11 7-11 7z" fill="#222"/></svg>
  </div>
  <form class="signup">
    <h4><svg width="16" height="16" viewBox="0 0 16 16"><rect x="1" y="3" width="12" height="12" rx="2" fill="none" stroke="#fff" stroke-width="1.5"/><path d="M6 10l1-3 7-6 2 2-7 6z" fill="#fff"/></svg>SUBSCRIBE NEWSLETTER SIGNUP</h4>
    <label>Your Name:</label>
    <div class="field"><span class="ico"><svg width="8" height="8" viewBox="0 0 8 8"><circle cx="4" cy="2.5" r="2" fill="#333"/><path d="M0 8c0-3 2-4 4-4s4 1 4 4z" fill="#333"/></svg></span><span>Your Name:</span></div>
    <label>Email Address:</label>
    <div class="field"><span class="ico"><svg width="8" height="6" viewBox="0 0 8 6"><rect width="8" height="6" fill="#333"/><path d="M0 0l4 3 4-3" fill="none" stroke="#fff" stroke-width=".8"/></svg></span><span>Email Address</span></div>
    <div class="agree"><span class="box"></span>I agree to Terms and Conditions <em>(Click open modal)</em></div>
    <div class="submit">NEWSLETTER SIGNUP</div>
  </form>
</section>

<section class="portfolio">
  <h2 class="section-title" style="top:955px">PORTFOLIO</h2>
  <p class="section-intro" style="top:977px">Lorem Ipsum is simply dummy text of the printing and typesetting industry. Lorem Ipsum has been the industry's standard dummy text ever since the 1500s, when an unknown.</p>
  <div class="carousel-arrow" style="left:39px"><svg width="24" height="24" viewBox="0 0 24 24"><path d="M14 7l-5 5 5 5" fill="none" stroke="#fff" stroke-width="2.5"/></svg></div>
  <div class="carousel-arrow" style="left:620px"><svg width="24" height="24" viewBox="0 0 24 24"><path d="M10 7l5 5-5 5" fill="none" stroke="#fff" stroke-width="2.5"/></svg></div>

  <div class="partner" style="left:74px">Norvale</div>
  <div class="partner" style="left:183px">Kestrel</div>
  <div class="partner" style="left:292px">Lumora</div>
  <div class="partner" style="left:401px">Velotrix</div>
  <div class="partner" style="left:510px">Halcyon</div>

  <div class="partner-name" style="left:74px">Norvale D/B/A</div>
  <div class="partner-name" style="left:183px">Kestrel Corp</div>
  <div class="partner-name" style="left:292px">Lumora Systems</div>
  <div class="partner-name" style="left:401px">Velotrix</div>
  <div class="partner-name" style="left:510px">Halcyon Inc</div>
</section>

<footer class="site-footer">
  <nav class="footer-nav"><span class="active">HOME</span><span>|</span><span>ABOUT US</span><span>|</span><span>PORTFOLIO</span><span>|</span><span>CONTACT</span></nav>
  <div class="copyright">©Tavell Corporation 2014 - All Right Reserved</div>
</footer>

</body>
</html>
```